B2B Service Company - Word Template

We need a word template to be used as business proposals for prospective clients. Please visit our web site: www.pandolin.com.do and our Instagram Pandolinrd for content / design ideas and to understand our branding and messaging . The color scheme must consistent with our logo, website and possibly our Instagram.

Just to be extra clear we expect the deliverable to be an actual working Microsoft word template document, with configured headers, theme, style, etc.

Target Market(s)

B2B Profesional companies

Requirements
Must have
• The color scheme must consistent with our logo, website and possibly our Instagram.

Different section headers, cover page with profesional design, back page, index section,

```html
<!DOCTYPE html>
<html lang="es">
<head>
<meta charset="utf-8">
<title>Pandolin – Proposal Covers</title>
<link href="https://fonts.googleapis.com/css2?family=Open+Sans:wght@300;400;700&display=swap" rel="stylesheet">
<style>
  :root {
    --backdrop: #ececec;
    --teal: #37b9cb;
    --ink: #0d0d0f;
    --paper: #ffffff;
    --stone: #c6c6c6;
  }
  html, body {
    margin: 0;
    padding: 0;
    width: 1200px;
    height: 1200px;
    overflow: hidden;
    background: var(--backdrop);
    font-family: "Open Sans", Arial, sans-serif;
  }
  .canvas {
    position: relative;
    width: 1200px;
    height: 1200px;
  }
  .cover {
    position: absolute;
    top: 233px;
    width: 457px;
    height: 647px;
    overflow: hidden;
    box-shadow: 6px 10px 22px rgba(0,0,0,0.28);
  }
  .cover--teal { left: 136px; background: var(--paper); }
  .cover--stone { left: 643px; background: var(--stone); }
  .cover-art {
    position: absolute;
    inset: 0;
    width: 457px;
    height: 647px;
  }
  .brand {
    position: absolute;
    font-family: "Open Sans", Arial, sans-serif;
    color: var(--ink);
  }
  .brand-name {
    display: block;
    font-weight: 700;
    letter-spacing: 0.04em;
    line-height: 1;
  }
  .brand-tagline {
    display: block;
    font-weight: 400;
    line-height: 1;
  }
  .cover--teal .brand {
    left: 0;
    right: 0;
    top: 72px;
    text-align: center;
  }
  .cover--teal .brand-name { font-size: 44px; }
  .cover--teal .brand-tagline { font-size: 17px; margin-top: 10px; }
  .cover--stone .brand {
    right: 35px;
    top: 42px;
    text-align: right;
  }
  .cover--stone .brand-name { font-size: 26px; }
  .cover--stone .brand-tagline { font-size: 11px; margin-top: 5px; }
  .cover-title {
    position: absolute;
    margin: 0;
    font-weight: 300;
    font-size: 20px;
    line-height: 25px;
    color: var(--paper);
    text-transform: uppercase;
  }
  .cover-subtitle {
    position: absolute;
    margin: 0;
    font-weight: 700;
    font-size: 13px;
    line-height: 18px;
    color: var(--ink);
    text-transform: uppercase;
  }
  .cover--teal .cover-title { left: 168px; top: 460px; }
  .cover--teal .cover-subtitle { left: 168px; top: 526px; }
  .cover--stone .cover-title { left: 35px; top: 509px; }
  .cover--stone .cover-subtitle { left: 35px; top: 575px; }
</style>
</head>
<body>
<main class="canvas">

  <section class="cover cover--teal">
    <svg class="cover-art" viewBox="0 0 457 647" aria-hidden="true">
      <rect x="0" y="189" width="457" height="458" fill="var(--teal)"/>
      <polygon points="304,189 344,189 0,610 0,562" fill="var(--paper)"/>
      <polygon points="0,394 0,444 164,647 205,647" fill="var(--ink)"/>
    </svg>
    <div class="brand">
      <span class="brand-name">PANDOLIN</span>
      <span class="brand-tagline">simplificando tu negocio</span>
    </div>
    <h1 class="cover-title">Lorem ipsum is simply<br>dummy has been</h1>
    <p class="cover-subtitle">Lorem ipsum is simply etiam<br>vestibulum</p>
  </section>

  <section class="cover cover--stone">
    <svg class="cover-art" viewBox="0 0 457 647" aria-hidden="true">
      <polygon points="225,0 285,0 0,350 0,276" fill="var(--paper)"/>
      <polygon points="234,0 275,0 0,337 0,287" fill="var(--teal)"/>
      <polygon points="0,110 0,182 368,647 440,647" fill="var(--paper)"/>
      <polygon points="0,120 0,172 380,647 422,647" fill="var(--ink)"/>
    </svg>
    <div class="brand">
      <span class="brand-name">PANDOLIN</span>
      <span class="brand-tagline">simplificando tu negocio</span>
    </div>
    <h1 class="cover-title">Lorem ipsum is simply<br>dummy has been</h1>
    <p class="cover-subtitle">Lorem ipsum is simply etiam<br>vestibulum</p>
  </section>

</main>
</body>
</html>
```